Steadfast MD - Sleep Medicine Specialist - Business Cards

We are a new medical practice called Steadfast MD. We are sleep medicine specialists and we will be conducting sleep studies on patients with sleep related ailments. We want the business card to be bold, professional, and clean with the logo as the stand out visual piece. We dont like wild flashy designs. We want our design to be bold and classic while at the same time conveying who we are and what we do. We are reliable, professional, and the best in the business.

Industry/Entity Type

Health Care

Contact Information for Business Card

- Clean
- Bold
- Classic
- not cluttered

Requirements
Must have
• logo, website, phone number
Nice to have
• several options to choose from
Should not have
• flashy imaged - reflective print - images of people sleeping

```html
<!DOCTYPE html>
<html lang="en">
<head>
<meta charset="utf-8">
<title>Steadfast MD – Business Cards</title>
<link rel="stylesheet" href="https://fonts.googleapis.com/css2?family=Poppins:wght@400;500;700;800&display=swap">
<style>
  :root {
    --backdrop: #2a2a2c;
    --card: #ffffff;
    --ink: #111111;
    --red: #e31b23;
    --ghost: #ececec;
  }
  * { box-sizing: border-box; margin: 0; padding: 0; }
  html, body { width: 1200px; height: 900px; overflow: hidden; }
  body {
    background: var(--backdrop);
    font-family: "Poppins", sans-serif;
    display: flex;
    flex-direction: column;
    align-items: center;
    justify-content: center;
    gap: 48px;
  }
  .card {
    position: relative;
    width: 560px;
    height: 320px;
    background: var(--card);
    border-radius: 22px;
    overflow: hidden;
  }

  /* Front */
  .front-ring {
    position: absolute;
    width: 250px; height: 250px;
    right: 40px; top: -40px;
    border: 10px solid var(--ghost);
    border-radius: 50%;
  }
  .front-brand {
    position: absolute;
    left: 0; right: 0; top: 50%;
    transform: translateY(-50%);
    display: flex;
    align-items: center;
    justify-content: center;
    gap: 14px;
  }
  .brand-dot {
    width: 58px; height: 58px;
    border: 4px solid var(--red);
    border-radius: 50%;
  }
  .brand-name {
    font-weight: 800;
    color: var(--ink);
    letter-spacing: -0.5px;
    line-height: 1;
  }
  .front-brand .brand-name { font-size: 42px; }

  /* Back */
  .back-ring {
    position: absolute;
    width: 300px; height: 300px;
    right: -30px; top: -20px;
    border: 9px solid var(--red);
    border-radius: 50%;
  }
  .back-content {
    position: absolute;
    left: 40px; top: 34px;
  }
  .back-content .brand-name { font-size: 40px; margin-bottom: 22px; }
  .person-name { font-weight: 700; font-size: 19px; color: var(--ink); line-height: 1.1; }
  .person-title { font-weight: 500; font-size: 13px; color: var(--red); margin-bottom: 12px; }
  .contact-list { list-style: none; }
  .contact-list li {
    display: flex;
    align-items: flex-start;
    gap: 10px;
    font-size: 12.5px;
    color: var(--ink);
    line-height: 1.45;
  }
  .contact-list svg { width: 13px; height: 13px; margin-top: 3px; flex: none; fill: var(--red); }
  .pulse-line {
    position: absolute;
    left: 0; bottom: 26px;
    width: 560px; height: 30px;
  }
</style>
</head>
<body>

<section class="card card-front" aria-label="Card front">
  <div class="front-ring"></div>
  <div class="front-brand">
    <span class="brand-dot"></span>
    <span class="brand-name">Steadfast MD</span>
  </div>
</section>

<section class="card card-back" aria-label="Card back">
  <div class="back-ring"></div>
  <div class="back-content">
    <div class="brand-name">Steadfast MD</div>
    <div class="person-name">Daniel Hart</div>
    <div class="person-title">Managing Director</div>
    <ul class="contact-list">
      <li><svg viewBox="0 0 24 24"><path d="M6.6 10.8a15 15 0 0 0 6.6 6.6l2.2-2.2a1 1 0 0 1 1-.25 11.4 11.4 0 0 0 3.6.57 1 1 0 0 1 1 1V20a1 1 0 0 1-1 1A17 17 0 0 1 3 4a1 1 0 0 1 1-1h3.5a1 1 0 0 1 1 1c0 1.25.2 2.45.57 3.57a1 1 0 0 1-.25 1z"/></svg>214 555 0187</li>
      <li><svg viewBox="0 0 24 24"><path d="M2 5h20v14H2z M4 7v.4l8 5.2 8-5.2V7z" fill-rule="evenodd"/></svg>daniel@steadfastmd.com</li>
      <li><svg viewBox="0 0 24 24"><path d="M12 2a10 10 0 1 0 0 20 10 10 0 0 0 0-20zm0 2c.9 1.2 1.6 2.6 2 4h-4c.4-1.4 1.1-2.8 2-4zM4.3 14a8 8 0 0 1 0-4h3.4a16 16 0 0 0 0 4zm.8 2h3c.3 1.3.8 2.5 1.5 3.6A8 8 0 0 1 5.1 16zm3-8h-3a8 8 0 0 1 4.5-3.6C8.9 5.5 8.4 6.7 8.1 8zM12 20c-.9-1.2-1.6-2.6-2-4h4c-.4 1.4-1.1 2.8-2 4zm2.3-6H9.7a14 14 0 0 1 0-4h4.6a14 14 0 0 1 0 4zm.1 5.6c.7-1.1 1.2-2.3 1.5-3.6h3a8 8 0 0 1-4.5 3.6zM16.3 14a16 16 0 0 0 0-4h3.4a8 8 0 0 1 0 4zm-.4-6c-.3-1.3-.8-2.5-1.5-3.6A8 8 0 0 1 18.9 8z"/></svg>www.steadfastmd.com</li>
      <li><svg viewBox="0 0 24 24"><path d="M12 2a7 7 0 0 0-7 7c0 5.2 7 13 7 13s7-7.8 7-13a7 7 0 0 0-7-7zm0 9.5A2.5 2.5 0 1 1 12 6.5a2.5 2.5 0 0 1 0 5z"/></svg><span>418 Alder Street NW<br>Suite 200, Fairhaven<br>MI 49012</span></li>
    </ul>
  </div>
  <svg class="pulse-line" viewBox="0 0 560 30" aria-hidden="true">
    <polyline points="0,24 120,24 128,12 134,28 140,6 146,20 152,18 560,18" fill="none" stroke="#e31b23" stroke-width="1.6"/>
  </svg>
</section>

</body>
</html>
```